Marisol Trevenko - Business Card Design

Hello everyone,

I need business cards designed to the following specs:

3.5"x2" with .25" bleed all around for printing
Square corners only

Please use attached business card for design reference.

Front:

Marisol Trevenko
Broker Associate

305-742-1186
marisoltrevenko@ quillmail.com (no space)
Instagram Logo @mtrevko
Facebook Logo Marisol Trevenko
4812 NW 127th St, Ste #210
Miami, Lakes, FL 33027

Back:

Brightway logo

Please submit editable AI, PDF, and JPG files.

Thanks and good luck!!!

```html
<!DOCTYPE html>
<html lang="en">
<head>
<meta charset="utf-8">
<title>Marisol Trevenko – Business Cards</title>
<link rel="stylesheet" href="https://fonts.googleapis.com/css2?family=Montserrat:wght@600&family=PT+Serif:wght@400;700&display=swap">
<style>
  :root {
    --backdrop: #1f2023;
    --card: #f3f3f2;
    --card-edge: #e2e2e0;
    --ink: #141414;
    --ink-soft: #3a3a3a;
    --ring: #111111;
    --photo-light: #e9d9c9;
    --photo-dark: #8a7466;
  }
  * { margin: 0; padding: 0; box-sizing: border-box; }
  html, body { width: 1200px; height: 800px; overflow: hidden; }
  body {
    background: var(--backdrop);
    display: flex;
    align-items: center;
    justify-content: center;
    gap: 40px;
  }
  .card {
    position: relative;
    width: 540px;
    height: 309px;
    background: linear-gradient(135deg, #f8f8f7, var(--card) 60%, var(--card-edge));
  }
  .wordmark {
    display: flex;
    align-items: center;
    gap: 12px;
    font-family: "Montserrat", sans-serif;
    font-weight: 600;
    color: var(--ink);
    letter-spacing: 0.08em;
  }
  .wordmark__square {
    width: 14px; height: 14px;
    background: var(--ink);
  }
  .card--brand .wordmark {
    position: absolute;
    top: 50%; left: 50%;
    transform: translate(-50%, -50%);
    font-size: 46px;
  }
  .card--brand .wordmark__square { width: 20px; height: 20px; }
  .card--contact .wordmark {
    position: absolute;
    left: 34px; top: 92px;
    font-size: 32px;
  }
  .portrait {
    position: absolute;
    right: 34px; top: 34px;
    width: 156px; height: 156px;
    border-radius: 50%;
    border: 9px solid var(--ring);
    background: radial-gradient(circle at 45% 40%, var(--photo-light), #cdb6a3 55%, var(--photo-dark));
  }
  .contact {
    position: absolute;
    left: 34px; top: 170px;
    font-family: "PT Serif", serif;
    color: var(--ink);
  }
  .contact__name {
    font-weight: 700;
    font-size: 15px;
    text-transform: uppercase;
    letter-spacing: 0.02em;
  }
  .contact__title { font-size: 13px; color: var(--ink-soft); margin-bottom: 3px; }
  .contact__address {
    font-size: 9px;
    text-transform: uppercase;
    line-height: 1.3;
    margin-bottom: 5px;
  }
  .contact__list { list-style: none; }
  .contact__item {
    display: flex;
    align-items: center;
    gap: 6px;
    font-size: 9px;
    text-transform: uppercase;
    line-height: 1.55;
  }
  .contact__icon { width: 11px; height: 11px; flex: none; }
</style>
</head>
<body>

  <section class="card card--brand" aria-label="Card back">
    <div class="wordmark"><span class="wordmark__square"></span>BRIGHTWAY</div>
  </section>

  <section class="card card--contact" aria-label="Card front">
    <div class="wordmark"><span class="wordmark__square"></span>BRIGHTWAY</div>

    <div class="portrait" role="img" aria-label="Portrait photo of the agent"></div>

    <div class="contact">
      <p class="contact__name">Marisol Trevenko</p>
      <p class="contact__title">Broker Associate</p>
      <p class="contact__address">4812 NW 127th St, Ste #210<br>Miami Lakes, FL 33027</p>
      <ul class="contact__list">
        <li class="contact__item">
          <svg class="contact__icon" viewBox="0 0 12 12" aria-label="Profile link">
            <circle cx="6" cy="6" r="6" fill="#141414"/>
            <rect x="2.6" y="4.9" width="4" height="2.2" rx="1.1" fill="none" stroke="#f3f3f2" stroke-width="0.8"/>
            <rect x="5.4" y="4.9" width="4" height="2.2" rx="1.1" fill="none" stroke="#f3f3f2" stroke-width="0.8"/>
          </svg>
          /marisoltrevenko
        </li>
        <li class="contact__item">
          <svg class="contact__icon" viewBox="0 0 12 12" aria-label="Social handle">
            <circle cx="6" cy="6" r="6" fill="#141414"/>
            <path d="M3 3.4 H9 V7.4 H5.4 L3.8 8.8 V7.4 H3 Z" fill="#f3f3f2"/>
          </svg>
          @mtrevko
        </li>
        <li class="contact__item">
          <svg class="contact__icon" viewBox="0 0 12 12" aria-label="Phone">
            <circle cx="6" cy="6" r="6" fill="#141414"/>
            <path d="M4 3.2 L5 3 L5.6 4.6 L4.9 5.2 Q5.5 6.6 6.8 7.1 L7.4 6.4 L9 7 L8.8 8 Q8.3 8.8 7 8.5 Q4.2 7.6 3.5 5 Q3.3 3.8 4 3.2 Z" fill="#f3f3f2"/>
          </svg>
          305-742-1186
        </li>
        <li class="contact__item">
          <svg class="contact__icon" viewBox="0 0 12 12" aria-label="Email">
            <circle cx="6" cy="6" r="6" fill="#141414"/>
            <rect x="3" y="4" width="6" height="4.2" fill="none" stroke="#f3f3f2" stroke-width="0.8"/>
            <path d="M3 4 L6 6.4 L9 4" fill="none" stroke="#f3f3f2" stroke-width="0.8"/>
          </svg>
          marisoltrevenko@quillmail.com
        </li>
      </ul>
    </div>
  </section>

</body>
</html>
```